Visitenkarten für ein Metallverarbeitsungsbetrieb
Zielgruppe
Metallverarbeitsungsbetrieb
spezialisiert auf Lasern
Aufgabenstellung
Passend zu unseren Logo und in den Farben, schlicht dennoch besonders

```html
<!DOCTYPE html>
<html lang="de">
<head>
<meta charset="utf-8">
<title>Vorka Laser GmbH – Visitenkarten</title>
<link rel="stylesheet" href="https://fonts.googleapis.com/css2?family=Barlow+Condensed:wght@400;500&display=swap">
<style>
  :root {
    --backdrop: #97d4d8;
    --card: #0e0d10;
    --accent: #1a86c2;
    --text: #ffffff;
    --brand-grey: #7a7a7a;
  }
  * { margin: 0; padding: 0; box-sizing: border-box; }
  html, body {
    width: 1200px;
    height: 1200px;
    overflow: hidden;
    background: var(--backdrop);
  }
  body {
    position: relative;
    font-family: "Barlow Condensed", "Arial Narrow", sans-serif;
    color: var(--text);
  }
  .card {
    position: absolute;
    left: 212px;
    width: 776px;
    height: 443px;
    background: var(--card);
  }
  .card--front { top: 141px; }
  .card--back { top: 616px; }

  .card__rule {
    position: absolute;
    left: 0;
    right: 0;
    top: 298px;
    height: 1.5px;
    background: var(--accent);
  }

  .brand {
    position: absolute;
    left: 78px;
    top: 128px;
    display: flex;
    align-items: center;
    gap: 16px;
  }
  .brand__dot {
    width: 40px;
    height: 40px;
    border-radius: 50%;
    background: var(--accent);
  }
  .brand__name {
    font-size: 46px;
    font-weight: 500;
    letter-spacing: 1px;
    color: var(--brand-grey);
    line-height: 1;
  }

  .tagline {
    position: absolute;
    left: 83px;
    top: 322px;
    font-size: 28px;
    font-weight: 400;
    line-height: 44px;
    letter-spacing: 0.3px;
  }

  .person {
    position: absolute;
    left: 85px;
    top: 208px;
    font-size: 44px;
    font-weight: 400;
    letter-spacing: 0.5px;
    line-height: 1;
  }

  .contact {
    position: absolute;
    top: 328px;
    font-size: 27px;
    font-weight: 400;
    line-height: 38px;
  }
  .contact--address { left: 83px; letter-spacing: 0.4px; }
  .contact--reach { left: 461px; letter-spacing: 1.6px; }
  .contact__label { margin-right: 10px; }

  .contact-divider {
    position: absolute;
    left: 388px;
    top: 329px;
    width: 1.5px;
    height: 80px;
    background: var(--accent);
  }
</style>
</head>
<body>
  <section class="card card--front">
    <div class="brand">
      <span class="brand__dot"></span>
      <span class="brand__name">VORKA LASER GMBH</span>
    </div>
    <div class="card__rule"></div>
    <p class="tagline">Metallverarbeitsungsbetrieb<br>Spezialisie rt auf Lasern</p>
  </section>

  <section class="card card--back">
    <h1 class="person">YOUR NAME</h1>
    <div class="card__rule"></div>
    <p class="contact contact--address">City name, Your Country<br>1234 Street name</p>
    <div class="contact-divider"></div>
    <p class="contact contact--reach"><span class="contact__label">P:</span>(123) 456789<br>name@yourcompany.de</p>
  </section>
</body>
</html>
```